FelixHarlan's Signature Beard Oil Label Design

I'm looking for a creative designer to run with the design. I am not sure what I really want so surprise me. What ever you do please use earth tone colors. The bottles I use is 2.0 ounces. It is a Boston amber bottle with glass dropper. It is 1.5 width by 3.75 inch height. :Benefits : * Organic * Hair growth* Repairs Split Ends* Softens * Health Shine* Aromatherapy fragrance* Reduce Itching/Irritation * Reduce Dandruff* Reduces Flyaway hair Directions: Place a nickel size drop into palm of handMassage into beard 2 to 3 times a day

Target Market(s)

MEN WITH BEARDS AND MEN THAT WANT TO GROW BEARDS BUT DON'T KNOW HOW

Industry/Entity Type

Hair Care Product

Font styles to use
Serif
Script

Colors
1b1b1b
fdf9cf
ffc214
ffffff

Requirements
Must have
• FALL COLOR SCHEME, Felix Harlan written in a fancy cursive script, all others can me different, please use the gold lion logo without the word Lion.
Nice to have
• CLASSY, MANLY, OLD AND NEW SCHOOL ESSENCE
Should not have
• Anything feminine, Pine Hollow

```html
<!DOCTYPE html>
<html lang="en">
<head>
<meta charset="utf-8">
<title>Felix Harlan Beard Oil Label</title>
<link rel="stylesheet" href="https://fonts.googleapis.com/css2?family=Kaushan+Script&family=Yellowtail&family=IM+Fell+English+SC&display=swap">
<style>
  :root {
    --kraft: #c9bb98;
    --kraft-dark: #c2b28e;
    --gold: #b8921a;
    --gold-bright: #c9a21e;
    --ink: #5e4c12;
    --ink-shadow: #f3ead0;
    --page: #ffffff;
  }
  html, body {
    margin: 0;
    padding: 0;
    width: 1200px;
    height: 1200px;
    overflow: hidden;
    background: var(--page);
  }
  .canvas {
    position: relative;
    width: 1200px;
    height: 1200px;
  }
  .label-art {
    position: absolute;
    inset: 0;
  }
  .script-title {
    position: absolute;
    font-family: "Kaushan Script", "Yellowtail", cursive;
    font-weight: 400;
    color: var(--gold-bright);
    text-shadow: 2px 2px 0 var(--ink);
    margin: 0;
    line-height: 1;
    transform: translate(-50%, -50%) rotate(-6deg);
    white-space: nowrap;
  }
  .panel-title { font-size: 62px; }
  .panel-list {
    position: absolute;
    margin: 0;
    padding: 0;
    list-style: none;
    font-family: "IM Fell English SC", serif;
    color: var(--ink);
    text-shadow: 1px 1px 0 var(--ink-shadow);
    text-align: center;
    transform: translateX(-50%);
    white-space: nowrap;
  }
  .directions-list {
    left: 248px;
    top: 224px;
    font-size: 34px;
    line-height: 54px;
  }
  .benefits-list {
    left: 939px;
    top: 212px;
    font-size: 26px;
    line-height: 37px;
  }
  .product-type {
    position: absolute;
    left: 603px;
    top: 124px;
    transform: translateX(-50%);
    margin: 0;
    font-family: "IM Fell English SC", serif;
    font-size: 38px;
    color: var(--ink);
    text-shadow: 1px 1px 0 var(--ink-shadow);
    white-space: nowrap;
    line-height: 1;
  }
  .brand-name { font-size: 92px; }
  .net-volume {
    position: absolute;
    left: 596px;
    top: 559px;
    transform: translateX(-50%);
    font-family: "IM Fell English SC", serif;
    font-size: 22px;
    color: var(--ink);
    text-decoration: underline;
    margin: 0;
  }
</style>
</head>
<body>
<main class="canvas">
  <svg class="label-art" width="1200" height="1200" viewBox="0 0 1200 1200" aria-hidden="true">
    <defs>
      <filter id="kraft-grain" x="0" y="0" width="100%" height="100%">
        <feTurbulence type="fractalNoise" baseFrequency="0.85" numOctaves="3" seed="7" result="noise"/>
        <feColorMatrix in="noise" type="matrix"
          values="0 0 0 0 0.30
                  0 0 0 0 0.26
                  0 0 0 0 0.18
                  2.2 0 0 0 -1.0" result="speckle"/>
        <feComposite in="speckle" in2="SourceGraphic" operator="in"/>
      </filter>
      <filter id="kraft-light" x="0" y="0" width="100%" height="100%">
        <feTurbulence type="fractalNoise" baseFrequency="0.6" numOctaves="2" seed="3" result="noise"/>
        <feColorMatrix in="noise" type="matrix"
          values="0 0 0 0 0.95
                  0 0 0 0 0.92
                  0 0 0 0 0.85
                  -2.4 0 0 0 1.0" result="fleck"/>
        <feComposite in="fleck" in2="SourceGraphic" operator="in"/>
      </filter>
    </defs>

    <!-- label paper -->
    <g class="label-paper">
      <rect x="33" y="109" width="1132" height="465" fill="var(--kraft)"/>
      <polygon points="451,62 747,62 747,595 599,680 451,595" fill="var(--kraft-dark)"/>
    </g>
    <g class="paper-grain" opacity="0.55" filter="url(#kraft-grain)">
      <rect x="33" y="109" width="1132" height="465" fill="#000"/>
      <polygon points="451,62 747,62 747,595 599,680 451,595" fill="#000"/>
    </g>
    <g class="paper-fleck" opacity="0.35" filter="url(#kraft-light)">
      <rect x="33" y="109" width="1132" height="465" fill="#000"/>
      <polygon points="451,62 747,62 747,595 599,680 451,595" fill="#000"/>
    </g>

    <!-- side wing frames -->
    <rect x="41" y="117" width="1116" height="449" fill="none" stroke="var(--gold)" stroke-width="2"/>
    <rect x="51" y="124" width="1096" height="435" fill="none" stroke="var(--gold)" stroke-width="3"/>
    <!-- banner body over the wing frames -->
    <polygon points="451,62 747,62 747,595 599,680 451,595" fill="var(--kraft-dark)" opacity="0.85"/>
    <g class="paper-grain" opacity="0.55" filter="url(#kraft-grain)">
      <polygon points="451,62 747,62 747,595 599,680 451,595" fill="#000"/>
    </g>
    <polygon points="470,91 728,91 728,567 599,650 470,567" fill="none" stroke="var(--gold)" stroke-width="4"/>
    <!-- BEARD OIL underline -->
    <line x1="497" y1="171" x2="711" y2="171" stroke="var(--ink)" stroke-width="2"/>
    <!-- swooshes -->
    <path d="M440,222 C520,235 600,190 690,196 C730,198 755,205 760,214" fill="none" stroke="var(--ink)" stroke-width="3"/>
    <path d="M440,230 C520,243 600,198 690,204 C730,206 752,212 756,218" fill="none" stroke="var(--ink)" stroke-width="1.5"/>
    <path d="M440,437 C520,460 600,408 690,410 C730,411 755,418 760,428" fill="none" stroke="var(--ink)" stroke-width="3"/>
    <path d="M440,445 C520,468 600,416 690,418 C730,419 752,425 756,431" fill="none" stroke="var(--ink)" stroke-width="1.5"/>
  </svg>

  <h2 class="script-title panel-title" style="left:245px; top:178px;">Directions</h2>
  <ol class="panel-list directions-list">
    <li>Place a nickel</li>
    <li>size drop into</li>
    <li>palm of hand</li>
    <li>Massage into</li>
    <li>beard 2 to 3</li>
    <li>times a day</li>
  </ol>

  <p class="product-type">BEARD OIL</p>
  <h1 class="script-title brand-name" style="left:584px; top:284px;">Felix</h1>
  <h1 class="script-title brand-name" style="left:625px; top:362px;">Harlan</h1>
  <p class="net-volume">2oz</p>

  <h2 class="script-title panel-title" style="left:940px; top:172px;">Benefits</h2>
  <ul class="panel-list benefits-list">
    <li>Organic</li>
    <li>Hair growth</li>
    <li>Repairs Split Ends</li>
    <li>Softens</li>
    <li>Health Shine</li>
    <li>Aromatherapy</li>
    <li>Reduce Itching/Irritation</li>
    <li>Reduce Dandruff</li>
    <li>Reduces Flyaway hair</li>
  </ul>
</main>
</body>
</html>
```